Financial firm simple design

Classic business card design for a financial fund. 2 sided card- white on both sides.. One with just the company name centered and the other w the info. info included on that is :

Name
Company position
phone number
fax
email
website

Industry/Entity Type

Financial

```html
<!DOCTYPE html>
<html lang="en">
<head>
<meta charset="utf-8">
<title>Northvale Investments – Business Card</title>
<link rel="stylesheet" href="https://fonts.googleapis.com/css2?family=Marcellus&family=Questrial&display=swap">
<style>
  :root {
    --backdrop: #e6e7e9;
    --card: #fbfbfc;
    --navy: #1f4a86;
    --ink: #2b2b2b;
    --muted: #5a5a5a;
    --band-grey: #a7a9ac;
    --band-blue: #1f4a86;
  }
  * { margin: 0; padding: 0; box-sizing: border-box; }
  html, body { width: 1200px; height: 800px; overflow: hidden; }
  body {
    background: var(--backdrop);
    display: flex;
    align-items: center;
    justify-content: center;
    gap: 40px;
  }
  .card {
    position: relative;
    width: 540px;
    height: 310px;
    background: var(--card);
    box-shadow: 0 6px 18px rgba(0,0,0,0.12);
    overflow: hidden;
  }
  .card-band {
    position: absolute;
    left: 0; right: 0; bottom: 0;
    height: 15px;
    display: flex;
    gap: 4px;
  }
  .card-band .band-grey { width: 36%; background: var(--band-grey); }
  .card-band .band-blue { flex: 1; background: var(--band-blue); }

  .wordmark {
    font-family: "Marcellus", serif;
    color: var(--navy);
    letter-spacing: 0.06em;
    white-space: nowrap;
  }
  .card-front .wordmark {
    position: absolute;
    top: 50%; left: 50%;
    transform: translate(-50%, -60%);
    font-size: 27px;
  }
  .card-back .wordmark {
    position: absolute;
    top: 56px; left: 50%;
    transform: translateX(-50%);
    font-size: 24px;
  }

  .contact-block {
    position: absolute;
    left: 34px; right: 24px;
    bottom: 38px;
    display: flex;
    align-items: flex-start;
    font-family: "Questrial", sans-serif;
  }
  .identity {
    text-align: right;
    padding-right: 14px;
  }
  .identity .person-name {
    color: var(--navy);
    font-size: 13px;
    font-weight: 700;
    letter-spacing: 0.05em;
  }
  .identity .person-title {
    color: var(--muted);
    font-size: 12px;
    margin-top: 2px;
  }
  .details {
    border-left: 1px solid #b9babc;
    padding-left: 12px;
    font-size: 11.5px;
    color: var(--muted);
    line-height: 1.45;
  }
  .details b { color: var(--navy); }
</style>
</head>
<body>
  <section class="card card-front" aria-label="Card front">
    <div class="wordmark">NORTHVALE INVESTMENTS</div>
    <div class="card-band"><span class="band-grey"></span><span class="band-blue"></span></div>
  </section>

  <section class="card card-back" aria-label="Card back">
    <div class="wordmark">NORTHVALE INVESTMENTS</div>
    <div class="contact-block">
      <div class="identity">
        <div class="person-name">MARK ELLISON</div>
        <div class="person-title">General Manager</div>
      </div>
      <div class="details">
        <div><b>T:</b> (555) 410-2730 · <b>F:</b> (555) 410-2731</div>
        <div><b>E:</b> mark@northvale.com · <b>W:</b> www.northvale.com</div>
      </div>
    </div>
    <div class="card-band"><span class="band-grey"></span><span class="band-blue"></span></div>
  </section>
</body>
</html>
```